Robotic Physical Therapy office needs a Grand Opening Flyer

We need a Grand Opening flyer design for a robotic physical therapy office named Kestrel Motion Therapy. We would like it to have a clean, classy, upscale feeling that gives potential clients a V.I.P. feeling. We would like to use the colors black, gray, and yellow (logo will be uploaded).

Event: Thursday, June 1st, 2023 from 12pm-6pm
location: 58240 Harlan Crest Ave, Pinegate Hollow, MI 48917

Industry/Entity Type

Physical therapy

Font styles to use
Script

Colors

Designer to choose colors to be used in the design.

Requirements
Nice to have
• More of a vip feel for the invite

```html
<!DOCTYPE html>
<html lang="en">
<head>
<meta charset="utf-8">
<title>Grand Opening – Kestrel Motion Therapy</title>
<link href="https://fonts.googleapis.com/css2?family=Great+Vibes&family=Allura&family=Source+Sans+3:wght@400;600;700&display=swap" rel="stylesheet">
<style>
  :root {
    --bg: #1e1e1f;
    --gold: #fedd10;
    --white: #ffffff;
  }
  * { margin: 0; padding: 0; box-sizing: border-box; }
  html, body { width: 927px; height: 1200px; overflow: hidden; background: var(--bg); }
  .flyer {
    position: relative;
    width: 927px;
    height: 1200px;
    background: var(--bg);
    color: var(--white);
    overflow: hidden;
  }
  .headline {
    position: absolute;
    left: 0;
    width: 100%;
    font-family: "Great Vibes", cursive;
    font-weight: 400;
    color: var(--gold);
    line-height: 1;
    white-space: nowrap;
  }
  .headline--grand {
    top: 150px;
    left: 90px;
    font-size: 250px;
  }
  .headline--opening {
    top: 335px;
    left: 110px;
    font-size: 250px;
  }
  .invitation {
    position: absolute;
    top: 658px;
    left: 60px;
    width: 807px;
    text-align: center;
    font-family: "Allura", cursive;
    font-size: 27px;
    line-height: 40px;
    color: var(--white);
  }
  .details {
    position: absolute;
    top: 933px;
    left: 0;
    width: 100%;
    text-align: center;
    font-family: "Source Sans 3", sans-serif;
    font-size: 16.5px;
    line-height: 22px;
    font-weight: 400;
    color: var(--white);
  }
  .details strong { font-weight: 700; }
  .brand {
    position: absolute;
    top: 1083px;
    left: 0;
    width: 100%;
    display: flex;
    justify-content: center;
    align-items: center;
    gap: 8px;
  }
  .brand__dot {
    width: 16px;
    height: 16px;
    border-radius: 50%;
    background: var(--gold);
  }
  .brand__name {
    font-family: "Source Sans 3", sans-serif;
    font-weight: 700;
    font-size: 20px;
    letter-spacing: 0.5px;
    color: var(--gold);
    text-transform: uppercase;
  }
</style>
</head>
<body>
  <main class="flyer">
    <h1>
      <span class="headline headline--grand">Grand</span>
      <span class="headline headline--opening">Opening</span>
    </h1>

    <p class="invitation">
      Come celebrate the grand opening of our state-of-the-art robotic physical therapy office!
      Our cutting-edge technology and highly skilled therapists provide personalized
      treatment plans to help you recover faster and more efficiently.
    </p>

    <div class="details">
      <p><strong>Event:</strong> Thursday, June 1st, 2023 from 12pm-6pm</p>
      <p><strong>Location:</strong> 58240 Harlan Crest Ave, Pinegate Hollow, MI 48917</p>
    </div>

    <div class="brand">
      <span class="brand__dot"></span>
      <span class="brand__name">Kestrel Motion Therapy</span>
    </div>
  </main>
</body>
</html>
```